I need a business Card Design for my practice , i am clinical herbalist. I am a herbalist specializing in Lyme disease, autism, autoimmune diseases, difficult to cure diseasesDifficult to cure diseases. In my innovative practice i link traditional medicine, herbs with science, immunologu ,pharmacology.

Industry/Entity Type

Business

Contact Information for Business Card

My company name : OŚRODEK ZIELNIK
My name : Piotr Kaleta
Name of my profession : Fitoterapeuta
In Polish language Fitoterapeuta is Herbalist .

e-mail: piotrkaleta@osrodekzielnik.com
www.osrodek-zielnik.pl
phone : 604 587 231
My company adress : Dąbrowa Sitnicka 41 , 38-415 Lużna
I dont have logo .

Requirements
Nice to have
• My company

```html
<!DOCTYPE html>
<html lang="pl">
<head>
<meta charset="utf-8">
<title>Ośrodek Zielnik – wizytówka</title>
<link href="https://fonts.googleapis.com/css2?family=Source+Sans+3:wght@400;600;700&display=swap" rel="stylesheet">
<style>
  :root {
    --stage: #1d1d1d;
    --paper: #ffffff;
    --leaf: #6ab42a;
    --bark: #7a4710;
    --ink: #1e1e1e;
    --sans: "Source Sans 3", "Open Sans", Arial, sans-serif;
  }
  * { box-sizing: border-box; margin: 0; padding: 0; }
  html, body { width: 1200px; height: 900px; overflow: hidden; }
  body { background: var(--stage); position: relative; font-family: var(--sans); }

  .card {
    position: absolute;
    top: 306px;
    width: 440px;
    height: 271px;
    border-radius: 12px;
    overflow: hidden;
  }
  .card--front { left: 149px; background: var(--paper); }
  .card--back { left: 608px; }

  .brand {
    position: absolute;
    left: 0; top: 0;
    width: 236px; height: 271px;
  }
  .brand__mark {
    position: absolute;
    left: 90px; top: 97px;
    width: 70px; height: 70px;
    border: 4px solid var(--leaf);
    border-radius: 50%;
  }
  .brand__name {
    position: absolute;
    left: 0; top: 174px;
    width: 250px;
    text-align: center;
    color: var(--leaf);
    font-size: 17px;
    font-weight: 400;
    letter-spacing: 0.3px;
    white-space: nowrap;
  }

  .divider {
    position: absolute;
    left: 236px; top: 77px;
    width: 1px; height: 120px;
    background: var(--bark);
  }

  .contact { position: absolute; left: 255px; top: 70px; width: 178px; color: var(--ink); }
  .contact__name {
    font-size: 16.5px; font-weight: 600; letter-spacing: 0.2px; line-height: 20px; white-space: nowrap;
  }
  .contact__first { color: var(--leaf); }
  .contact__last { color: var(--bark); }
  .contact__role { font-size: 12.5px; line-height: 15px; }
  .contact__lines { margin-top: 24px; font-size: 12px; line-height: 16px; }
  .contact__line { display: flex; align-items: center; gap: 6px; white-space: nowrap; }
  .contact__line--email { font-size: 11.5px; }
  .contact__line svg { width: 8px; height: 8px; flex: none; }
  .contact__address { margin-top: 8px; font-size: 12.5px; line-height: 16px; }

  .back__pattern {
    position: absolute; inset: 0;
    background: var(--leaf);
  }
  .back__brand {
    position: absolute; inset: 0;
    display: flex; flex-direction: column; align-items: center; justify-content: center;
    gap: 16px;
  }
  .back__mark {
    width: 110px; height: 110px;
    border: 6px solid var(--paper);
    border-radius: 50%;
  }
  .back__name {
    color: var(--paper);
    font-size: 20px; font-weight: 600; letter-spacing: 1px;
  }
</style>
</head>
<body>

<section class="card card--front">
  <div class="brand">
    <div class="brand__mark"></div>
    <div class="brand__name">OŚRODEK ZIELNIK</div>
  </div>
  <div class="divider"></div>
  <div class="contact">
    <div class="contact__name"><span class="contact__first">PIOTR</span> <span class="contact__last">KALETA</span></div>
    <div class="contact__role">Fitoterapeuta</div>
    <div class="contact__lines">
      <div class="contact__line">
        <svg viewBox="0 0 10 10"><path fill="var(--leaf)" d="M2 0.5 3.6 2.6 2.6 3.8C3.3 5.3 4.6 6.6 6.2 7.4L7.4 6.4 9.5 8 8.6 9.5C4.4 9.2 0.8 5.6 0.5 1.4Z"/></svg>
        <span>604 587 231</span>
      </div>
      <div class="contact__line contact__line--email">
        <svg viewBox="0 0 10 10"><rect x="0.5" y="1.5" width="9" height="7" fill="var(--leaf)"/><path d="M0.5 1.8 5 5.4 9.5 1.8" fill="none" stroke="#fff" stroke-width="1"/></svg>
        <span>piotrkaleta@osrodekzielnik.com</span>
      </div>
    </div>
    <div class="contact__address">Dąbrowa Sitnicka 41,<br>38-415 Lużna</div>
  </div>
</section>

<section class="card card--back">
  <div class="back__pattern" role="img" aria-label="Zielone tło z delikatnym, powtarzającym się wzorem ziołowym"></div>
  <div class="back__brand">
    <div class="back__mark"></div>
    <div class="back__name">OŚRODEK ZIELNIK</div>
  </div>
</section>

</body>
</html>
```